Computer repair shop

A card with our logo. And number and email and address. Our colors are baby /light blue and gray

Prefferably one sode with full logo - interested in other designs and options

Computer / mac repair shop
On site support
Snall business IT support

```html
<!DOCTYPE html>
<html lang="en">
<head>
<meta charset="utf-8">
<title>Byte Fixers – Business Card</title>
<link href="https://fonts.googleapis.com/css2?family=Montserrat:wght@400;500;700;900&display=swap" rel="stylesheet">
<style>
  :root {
    --page: #e7e8ea;
    --card-dark: #2a2d31;
    --card-light: #ffffff;
    --brand-blue: #1a8fd6;
    --text-light: #ffffff;
    --text-gray: #5a5d61;
    --text-dark: #3a3c40;
    --mascot-blue: #2e9be0;
    --mascot-gray: #5b5e63;
  }
  * { box-sizing: border-box; margin: 0; padding: 0; }
  html, body {
    width: 1200px; height: 716px; overflow: hidden;
    background: var(--page);
    font-family: "Montserrat", Arial, sans-serif;
  }
  .canvas {
    position: relative; width: 1200px; height: 716px;
    display: flex; align-items: center; justify-content: center; gap: 24px;
  }
  .card {
    position: relative; width: 540px; height: 308px;
    box-shadow: 0 8px 24px rgba(0,0,0,.18);
    overflow: hidden;
  }
  /* Front */
  .card--front { background: var(--card-dark); color: var(--text-light); }
  .services { position: absolute; left: 34px; top: 30px; list-style: none; }
  .services li {
    display: flex; align-items: center; gap: 10px;
    font-size: 17px; font-weight: 500; letter-spacing: .3px; line-height: 26px;
  }
  .services svg { width: 18px; height: 18px; flex: none; }
  .brand {
    position: absolute; left: 0; right: 0; bottom: 56px;
    display: flex; align-items: center; justify-content: center; gap: 12px;
  }
  .brand__mark { width: 22px; height: 22px; background: var(--brand-blue); }
  .brand__name {
    font-size: 44px; font-weight: 900; letter-spacing: -.5px;
    color: var(--text-light); text-transform: uppercase;
  }
  /* Back */
  .card--back { background: var(--card-light); color: var(--text-gray); }
  .contact { position: absolute; left: 34px; bottom: 52px; font-size: 13.5px; line-height: 20px; }
  .contact__address { margin-bottom: 14px; }
  .contact__row { display: flex; align-items: center; gap: 10px; }
  .contact__row svg { width: 12px; height: 12px; flex: none; }
  .person {
    position: absolute; right: 44px; top: 44px; text-align: right;
    white-space: nowrap;
  }
  .person__name { font-size: 24px; font-weight: 500; color: var(--brand-blue); line-height: 28px; }
  .person__role { font-size: 16px; font-weight: 400; color: var(--text-dark); margin-top: 2px; }
  .mascot {
    position: absolute; left: 300px; top: 118px; width: 180px; height: 160px;
    border-radius: 14px;
    background: linear-gradient(160deg, var(--mascot-blue) 0%, #6fbbe9 55%, var(--mascot-gray) 100%);
  }
</style>
</head>
<body>
<main class="canvas">
  <section class="card card--front">
    <ul class="services">
      <li><svg viewBox="0 0 18 18"><path d="M2 10 L7 15 L16 3" fill="none" stroke="#1a8fd6" stroke-width="3" stroke-linecap="round"/></svg>Computer / mac repair shop</li>
      <li><svg viewBox="0 0 18 18"><path d="M2 10 L7 15 L16 3" fill="none" stroke="#1a8fd6" stroke-width="3" stroke-linecap="round"/></svg>On site support</li>
      <li><svg viewBox="0 0 18 18"><path d="M2 10 L7 15 L16 3" fill="none" stroke="#1a8fd6" stroke-width="3" stroke-linecap="round"/></svg>Snall business IT support</li>
    </ul>
    <div class="brand">
      <span class="brand__mark"></span>
      <span class="brand__name">Byte Fixers</span>
    </div>
  </section>

  <section class="card card--back">
    <div class="person">
      <p class="person__name">Alex Morgan</p>
      <p class="person__role">Director</p>
    </div>
    <div class="contact">
      <p class="contact__address">45 Harbor Lane<br>Lakeview, AB, T2X 4K9</p>
      <p class="contact__row"><svg viewBox="0 0 12 12"><path d="M3 1 L5 3 L4 5 Q5 7 7 8 L9 7 L11 9 L9 11 Q2 10 1 3 Z" fill="#1a8fd6"/></svg>555-204-3178</p>
      <p class="contact__row"><svg viewBox="0 0 12 12"><rect x="1" y="2.5" width="10" height="7" fill="#1a8fd6"/><path d="M1 2.5 L6 6.5 L11 2.5" fill="none" stroke="#fff" stroke-width="1"/></svg>alex.morgan@bytefixers.com</p>
      <p class="contact__row"><svg viewBox="0 0 12 12"><circle cx="6" cy="6" r="5" fill="none" stroke="#1a8fd6" stroke-width="1.4"/><path d="M1 6 H11 M6 1 Q3 6 6 11 M6 1 Q9 6 6 11" fill="none" stroke="#1a8fd6" stroke-width="1"/></svg>www.bytefixers.com</p>
    </div>
    <div class="mascot" role="img" aria-label="Cartoon computer monitor mascot in blue and gray, waving and holding a screwdriver"></div>
  </section>
</main>
</body>
</html>
```